Sales/Landing Page Redesign for Hunting product

I am looking for a redesign for https://ridgeholloworchard.com/quarter-pad .

We want to add in the information for our new XL quarterpad found: https://ridgeholloworchard.com/shop/hunting/xl-big-game-quarter-pad/

We also will be adding a spot for this video: https://www.vidstreamer.example/watch?v=Zt7kLq2wPnx

We like having the 3 options at the bottom, but the goal for this page is to sell the quarter pad.

Target Market(s)

Western Hunters, campers, outdoorsmen

Industry/Entity Type

Hunting

Number of Pages Required

1 page

Font styles to use
Sans Serif

Requirements
Must have
• a clean design that is geared to sell the product.

```html
<!DOCTYPE html>
<html lang="en">
<head>
<meta charset="utf-8">
<title>Trailhold Quarter Pads</title>
<link href="https://fonts.googleapis.com/css2?family=Lexend:wght@300;400;500;600&display=swap" rel="stylesheet">
<style>
:root{
  --red:#d20a0a;
  --ink:#111111;
  --muted:#555555;
  --panel:#f1f1f1;
  --tile:#eeeeee;
  --sand:#d9d1c7;
  --white:#ffffff;
}
*{box-sizing:border-box;margin:0;padding:0}
html,body{width:1200px;height:4847px;overflow:hidden;background:var(--white)}
body{font-family:"Lexend",sans-serif;color:var(--ink);position:relative}
.abs{position:absolute}
.center{text-align:center}
.btn{position:absolute;display:flex;align-items:center;justify-content:center;font-size:13px;font-weight:600;color:var(--white);border-radius:3px;text-decoration:none}
.btn-red{background:var(--red)}
.btn-dark{background:var(--ink)}
.brand{font-weight:600;color:var(--red);letter-spacing:3px}

/* header */
.site-header .brand{left:80px;top:58px;font-size:30px}
.nav a{position:absolute;top:60px;font-size:14px;color:var(--ink);text-decoration:none}
.nav .active{border-bottom:2px solid var(--red);padding-bottom:8px}
.nav .shop{color:var(--red)}

/* hero */
.hero-title{left:80px;top:212px;font-size:54px;line-height:61px;font-weight:300}
.hero-title b{font-weight:500}
.hero-list{left:82px;top:416px;width:186px}
.hero-list li{list-style:none;font-size:19px;padding:4px 0 7px;border-bottom:1px solid #e9a0a0;margin-bottom:6px}
.hero-list li:last-child{border:none}
.hero-photo{left:481px;top:150px;width:640px;height:527px;background:linear-gradient(135deg,#3c2a20 0%,#e86a1b 35%,#f08a2a 55%,#6b4a3d 75%,#2a2624 100%)}

/* still section */
.still{left:0;top:749px;width:1200px;height:803px;background:var(--panel)}
.section-title{position:absolute;left:0;width:1200px;text-align:center;font-weight:400;font-size:40px}
.lead{position:absolute;left:200px;width:800px;text-align:center;font-size:13.5px;line-height:23px;font-weight:300;color:#333}
.habit{position:absolute;width:326px;height:147px;border:2px solid var(--red);border-radius:2px;display:flex;align-items:center;justify-content:center;text-align:center;font-size:21px;line-height:32px;padding-top:10px}
.habit svg{position:absolute;left:102px;top:-26px}
.better{font-size:27px;top:1392px}

/* features */
.tile{position:absolute;width:329px;height:272px;background:var(--tile);display:flex;flex-direction:column;align-items:center;justify-content:flex-end;padding-bottom:58px;text-align:center;font-size:20px;line-height:28px}
.tile svg{margin-bottom:26px}
.tile.featured{background:var(--red);color:var(--white);font-weight:500}

/* products */
.product-card{position:absolute;top:2620px;height:311px;border:2px solid #dcdcdc;background:var(--white)}
.product-photo{position:absolute;left:60px;top:50px;width:210px;height:210px;border-radius:30px 30px 18px 18px}
.heart{position:absolute;right:16px;top:14px}
.tag{position:absolute;left:0;top:0;background:var(--ink);color:var(--white);font-size:12px;font-weight:600;padding:4px 8px}
.size{position:absolute;top:2946px;font-size:13px;color:var(--muted);display:flex;gap:8px;align-items:center}
.size span{border:1px solid #999;width:22px;height:22px;display:flex;align-items:center;justify-content:center;font-size:12px}
.size span.on{background:#444;color:var(--white);border-color:#444}
.pname{position:absolute;top:2990px;font-size:19px;text-align:center}
.price{position:absolute;top:3024px;font-size:23px;color:var(--red);text-align:center}
.price s{font-size:16px;color:#999;margin-left:22px}

/* guarantee */
.guarantee{left:0;top:3226px;width:1200px;height:395px;background:linear-gradient(120deg,#b80c08,#e2251a 45%,#a60a06 80%,#c81510)}
.guarantee h2{position:absolute;left:0;top:3442px;width:1200px;text-align:center;color:var(--white);font-size:41px;font-weight:500}
.guarantee p{position:absolute;left:190px;top:3510px;width:820px;text-align:center;color:var(--white);font-size:14px;line-height:25px;font-weight:300}

/* video */
.video{left:71px;top:3694px;width:1043px;height:533px;background:linear-gradient(180deg,#a9aaa9 0%,#8a8d86 40%,#4f5a3e 70%,#3b4231 100%)}

/* testimonials */
.reviews{left:0;top:4287px;width:1200px;height:355px;background:var(--panel)}
.quote{position:absolute;left:300px;top:4440px;width:600px;text-align:center;font-size:14px;line-height:23px;color:var(--red);font-weight:300}
.arrow{position:absolute;top:4444px;width:40px;height:40px;border-radius:50%;background:var(--white);display:flex;align-items:center;justify-content:center}

/* footer */
.site-footer{left:0;top:4642px;width:1200px;height:205px;background:var(--sand)}
.site-footer .brand{left:84px;top:4730px;font-size:34px}
.footer-links{position:absolute;left:864px;top:4672px;width:240px;text-align:center;font-size:14px;line-height:29.5px;list-style:none}
.copy{position:absolute;left:440px;top:4765px;width:320px;text-align:center;font-size:12px}
.social{position:absolute;left:546px;top:4732px;display:flex;gap:8px}
.social span{width:24px;height:24px;border-radius:50%;background:var(--ink);display:block}
</style>
</head>
<body>

<header class="site-header">
  <div class="abs brand">TRAILHOLD</div>
  <nav class="nav">
    <a class="active" style="left:668px">Meals</a>
    <a style="left:752px">Quarter Pads</a>
    <a style="left:886px">Contact</a>
    <a class="shop" style="left:985px">Shop Now</a>
    <svg class="abs" style="left:1092px;top:55px" width="26" height="24" viewBox="0 0 26 24" fill="none" stroke="#d20a0a" stroke-width="2"><path d="M1 2h4l3 13h13l3-9H7"/><circle cx="10" cy="20" r="2"/><circle cx="19" cy="20" r="2"/></svg>
  </nav>
</header>

<section class="hero">
  <h1 class="abs hero-title"><b>Quarter Pads</b><br>to keep your<br><b>Meat Clean</b></h1>
  <ul class="abs hero-list"><li>100% Waterproof</li><li>Lightweight</li><li>Quality Guarantee</li></ul>
  <a class="btn btn-red" style="left:80px;top:563px;width:143px;height:48px">Learn More</a>
  <a class="btn btn-dark" style="left:242px;top:563px;width:143px;height:48px">Buy Now</a>
  <div class="abs hero-photo" role="img" aria-label="Fresh game quarters laid on an orange quarter pad outdoors"></div>
</section>

<section class="abs still"></section>
<h2 class="section-title" style="top:806px">Do You Still...</h2>
<p class="lead" style="top:878px">Lorem Ipsum is simply dummy text of the printing and typesetting industry. Lorem Ipsum has been the industry's standard dummy text ever since the 1500s.</p>

<div class="habit" style="left:83px;top:988px"><svg width="120" height="62" viewBox="0 0 120 62" fill="none" stroke="#d20a0a" stroke-width="3"><path d="M0 26 L60 60 L120 26" stroke-width="2"/><path d="M40 20 L55 36 L86 4"/></svg>Lay your fresh<br>meat on a rock?</div>
<div class="habit" style="left:438px;top:988px"><svg width="120" height="62" viewBox="0 0 120 62" fill="none" stroke="#d20a0a" stroke-width="3"><path d="M0 26 L60 60 L120 26" stroke-width="2"/><path d="M40 20 L55 36 L86 4"/></svg>Sew bed sheets<br>together?</div>
<div class="habit" style="left:792px;top:988px"><svg width="120" height="62" viewBox="0 0 120 62" fill="none" stroke="#d20a0a" stroke-width="3"><path d="M0 26 L60 60 L120 26" stroke-width="2"/><path d="M40 20 L55 36 L86 4"/></svg>Use a blue tarp?</div>
<div class="habit" style="left:261px;top:1194px"><svg width="120" height="62" viewBox="0 0 120 62" fill="none" stroke="#d20a0a" stroke-width="3"><path d="M0 26 L60 60 L120 26" stroke-width="2"/><path d="M40 20 L55 36 L86 4"/></svg>Lay your meat<br>in the dirt?</div>
<div class="habit" style="left:617px;top:1194px"><svg width="120" height="62" viewBox="0 0 120 62" fill="none" stroke="#d20a0a" stroke-width="3"><path d="M0 26 L60 60 L120 26" stroke-width="2"/><path d="M40 20 L55 36 L86 4"/></svg>Stuff the meat in old<br>used pillow cases?</div>

<p class="section-title better">...There is a better way</p>
<a class="btn btn-red" style="left:491px;top:1450px;width:218px;height:49px">Select my Quarter Pad</a>

<h2 class="section-title" style="top:1614px">Be responsible. Use a quarter pad.</h2>
<p class="lead" style="top:1688px">Lorem Ipsum is simply dummy text of the printing and typesetting industry. Lorem Ipsum has been the industry's standard dummy text ever since the 1500s.</p>

<div class="tile featured" style="left:79px;top:1774px">
  <svg width="90" height="90" viewBox="0 0 90 90" fill="none" stroke="#fff" stroke-width="3"><ellipse cx="36" cy="36" rx="26" ry="22" transform="rotate(-30 36 36)"/><circle cx="30" cy="36" r="7"/><path d="M54 54 L72 74"/><circle cx="76" cy="78" r="5"/></svg>
  Keep your meat off<br>the dirt</div>
<div class="tile" style="left:436px;top:1774px">
  <svg width="90" height="90" viewBox="0 0 90 90" fill="none" stroke-width="3"><path d="M20 52 A26 26 0 0 1 40 18 l-6 -8 M40 18 l-9 4" stroke="#111"/><path d="M56 20 A26 26 0 0 1 72 50 l8 -4 M72 50 l-2 -10" stroke="#111"/><path d="M64 66 A26 26 0 0 1 28 68 l2 8 M28 68 l10 -2" stroke="#d20a0a"/></svg>
  Reusable</div>
<div class="tile" style="left:792px;top:1774px">
  <svg width="110" height="90" viewBox="0 0 110 90" fill="none" stroke-width="3"><path d="M20 40 C40 10 80 8 96 6 C86 30 60 50 22 48 Z" stroke="#d20a0a"/><path d="M22 48 L70 22" stroke="#d20a0a"/><path d="M8 78 H104" stroke="#111"/><path d="M14 70 H100" stroke="#111" stroke-dasharray="3 6"/></svg>
  Lightweight</div>
<div class="tile" style="left:76px;top:2077px">
  <svg width="80" height="80" viewBox="0 0 80 80" fill="none" stroke-width="4"><path d="M8 8 L30 30 M8 8 h14 M8 8 v14" stroke="#d20a0a"/><path d="M72 8 L50 30 M72 8 h-14 M72 8 v14" stroke="#111"/><path d="M8 72 L30 50 M8 72 h14 M8 72 v-14" stroke="#111"/><path d="M72 72 L50 50 M72 72 h-14 M72 72 v-14" stroke="#d20a0a"/></svg>
  55"x60" when open</div>
<div class="tile" style="left:436px;top:2077px">
  <svg width="90" height="100" viewBox="0 0 90 100" fill="none" stroke-width="3"><path d="M60 6 C50 24 42 34 42 46 a18 18 0 0 0 36 0 C78 34 70 24 60 6Z" stroke="#d20a0a"/><path d="M20 40 C14 50 10 56 10 62 a10 10 0 0 0 20 0 C30 56 26 50 20 40Z" stroke="#111"/><path d="M36 70 C32 78 30 82 30 86 a7 7 0 0 0 14 0 C44 82 40 78 36 70Z" stroke="#111"/></svg>
  100% waterproof</div>
<div class="tile" style="left:792px;top:2077px;padding-bottom:42px">
  <svg width="90" height="90" viewBox="0 0 90 90" fill="none" stroke-width="3"><ellipse cx="26" cy="16" rx="8" ry="10" stroke="#111"/><ellipse cx="50" cy="14" rx="8" ry="10" stroke="#111"/><ellipse cx="70" cy="34" rx="8" ry="10" stroke="#111"/><ellipse cx="72" cy="62" rx="7" ry="9" stroke="#111"/><path d="M20 50 C30 30 50 34 54 52 C58 70 44 78 32 74 C18 72 12 62 20 50Z" stroke="#d20a0a"/></svg>
  Respect the animal by<br>keeping it contamination free.</div>

<a class="btn btn-red" style="left:491px;top:2395px;width:218px;height:48px">Select my Quarter Pad</a>

<h2 class="section-title" style="top:2518px">Choose a quarter pad</h2>

<div class="product-card" style="left:79px;width:329px">
  <svg class="heart" width="20" height="18" viewBox="0 0 20 18" fill="none" stroke="#111" stroke-width="1.5"><path d="M10 16 C4 11 1 8 1 5 a4 4 0 0 1 9 -1 a4 4 0 0 1 9 1 c0 3-3 6-9 11z"/></svg>
  <div class="product-photo" style="background:linear-gradient(160deg,#e23a2c,#b4160f)" role="img" aria-label="Red packed quarter pad in its stuff sack"></div>
</div>
<div class="product-card" style="left:436px;width:329px">
  <span class="tag">New XL Size</span>
  <svg class="heart" width="20" height="18" viewBox="0 0 20 18" fill="none" stroke="#111" stroke-width="1.5"><path d="M10 16 C4 11 1 8 1 5 a4 4 0 0 1 9 -1 a4 4 0 0 1 9 1 c0 3-3 6-9 11z"/></svg>
  <div class="product-photo" style="background:linear-gradient(160deg,#ff8a3a,#e8611a)" role="img" aria-label="Orange XL quarter pad in its stuff sack"></div>
</div>
<div class="product-card" style="left:787px;width:334px">
  <svg class="heart" width="20" height="18" viewBox="0 0 20 18" fill="none" stroke="#111" stroke-width="1.5"><path d="M10 16 C4 11 1 8 1 5 a4 4 0 0 1 9 -1 a4 4 0 0 1 9 1 c0 3-3 6-9 11z"/></svg>
  <div class="product-photo" style="background:linear-gradient(160deg,#2fcf78,#17a658)" role="img" aria-label="Green packed quarter pad in its stuff sack"></div>
</div>

<div class="size" style="left:188px">Size <span>M</span></div>
<div class="size" style="left:543px">Size <span>M</span><span class="on">XL</span></div>
<div class="size" style="left:908px">Size <span>M</span></div>

<p class="pname" style="left:79px;width:329px">Red Quarter Pad</p>
<p class="pname" style="left:436px;width:329px">Orange Quarter Pad</p>
<p class="pname" style="left:787px;width:334px">Green Quarter Pad</p>
<p class="price" style="left:79px;width:329px">$ 19.99<s>$ 21.99</s></p>
<p class="price" style="left:436px;width:329px">$ 19.99<s>$ 21.99</s></p>
<p class="price" style="left:787px;width:334px">$ 19.99<s>$ 21.99</s></p>
<a class="btn btn-red" style="left:171px;top:3081px;width:143px;height:48px">Buy Now</a>
<a class="btn btn-dark" style="left:532px;top:3081px;width:143px;height:48px">Buy Now</a>
<a class="btn btn-dark" style="left:882px;top:3081px;width:143px;height:48px">Buy Now</a>

<section class="abs guarantee" role="img" aria-label="Red quarter pad spread on the ground behind a red tint"></section>
<svg class="abs" style="left:552px;top:3299px" width="96" height="118" viewBox="0 0 96 118" fill="none" stroke="#fff" stroke-width="3"><circle cx="48" cy="44" r="40"/><circle cx="48" cy="44" r="30"/><path d="M48 26 l5 11 12 1 -9 8 3 12 -11-6 -11 6 3-12 -9-8 12-1z"/><path d="M28 78 L16 110 l12-6 6 12 10-30 M68 78 L80 110 l-12-6 -6 12 -10-30"/></svg>
<h2 class="guarantee-title" style="position:absolute;left:0;top:3442px;width:1200px;text-align:center;color:#fff;font-size:41px;font-weight:500">100% Quality Guarantee</h2>
<p style="position:absolute;left:190px;top:3510px;width:820px;text-align:center;color:#fff;font-size:14px;line-height:25px;font-weight:300">We've designed our Quarter Pads for maximum performance and durability so you can keep the meat you harvest in the backcountry clean and out of the dirt. If you are at all unsatisfied, contact us and we'll make it right.</p>

<section class="abs video" role="img" aria-label="Video still of a hunter in camouflage beside a spotting scope in the hills"></section>
<svg class="abs" style="left:71px;top:3694px" width="1043" height="533" viewBox="0 0 1043 533">
  <circle cx="526" cy="267" r="50" fill="rgba(0,0,0,0.55)"/>
  <path d="M510 245 L545 267 L510 289Z" fill="#fff"/>
  <rect x="30" y="470" width="1000" height="4" fill="rgba(255,255,255,0.35)"/>
  <rect x="30" y="470" width="497" height="4" fill="#e01010"/>
  <circle cx="527" cy="472" r="7" fill="#e01010"/>
  <rect x="590" y="470" width="8" height="4" fill="#f2c200"/>
  <rect x="785" y="470" width="42" height="4" fill="#f2c200"/>
  <rect x="990" y="470" width="8" height="4" fill="#f2c200"/>
  <g fill="none" stroke="#fff" stroke-width="2">
    <rect x="776" y="497" width="18" height="13"/>
    <circle cx="822" cy="503" r="6"/>
    <rect x="850" y="496" width="20" height="14"/>
    <rect x="890" y="498" width="24" height="11"/>
    <path d="M932 498 h20 v12 h-8 M932 504 a6 6 0 0 1 6 6"/>
    <path d="M972 497 h-5 v5 M987 497 h5 v5 M972 511 h-5 v-5 M987 511 h5 v-5"/>
  </g>
</svg>

<section class="abs reviews"></section>
<h2 class="section-title" style="top:4334px">What others are saying...</h2>
<p class="quote">Gone are the days of struggling to keep a quarter from sliding off a log or rock while trying to de-bone meat. Packs small, weighs nothing, and keeps meat perfectly clean. It's in my pack 100% of the time. Great Product!</p>
<p class="abs center" style="left:0;width:1200px;top:4540px;font-size:18px">Morgan Reyes</p>
<div class="arrow" style="left:86px"><svg width="14" height="18" viewBox="0 0 14 18" fill="none" stroke="#d20a0a" stroke-width="2.5"><path d="M10 2 L3 9 L10 16"/></svg></div>
<div class="arrow" style="left:1069px"><svg width="14" height="18" viewBox="0 0 14 18" fill="none" stroke="#d20a0a" stroke-width="2.5"><path d="M4 2 L11 9 L4 16"/></svg></div>

<footer class="abs site-footer"></footer>
<div class="abs brand" style="left:84px;top:4730px;font-size:34px">TRAILHOLD</div>
<div class="social"><span></span><span></span><span></span></div>
<p class="copy">© 2020 Trailhold . All rights reserved</p>
<ul class="footer-links"><li>My Account</li><li>Blog</li><li>Terms of Service Agreement</li><li>Refund and Return Policy</li><li>Privacy Policy Agreement</li></ul>

</body>
</html>
```